Brightvale Cherries Rainier POS Card 7"H x 11"W

We are wanting to create a one-sided 7 x 11 Rainier cherry card that is eye catching and informative.This should be clear and easy to read and not cluttered. We use these cards as a display in grocery stores, demo stands, and other events to market Brightvale Rainier Cherries. We have a few facts that we would like displayed on the card (see below).

Target Market(s)

Consumers

Industry/Entity Type

Agriculture

Font styles to use
Sans Serif

Requirements
Must have
• Yellow cherries - yellow fruit (the blush on the skin is a kiss from the sun)
• Juice doesn't stain - Kid Friendly
• Add contrast to your summer table
• Sweetest Variety - still low glycemic
• Source of Vitamin C, Source of Potassium, and Source of Melatonin
• Rainiers take up to 4x as much work as red cherries
• Natural Color palettes
• Easy to read
• Brightvale Cherries
Nice to have
• Unique, creative, realistc Rainier cherry designs
Should not have
• pastel or neon color scheme, overly cutesy elements

```html
<!DOCTYPE html>
<html lang="en">
<head>
<meta charset="utf-8">
<title>Brightvale Cherries – Yellow Cherries Card</title>
<link rel="stylesheet" href="https://fonts.googleapis.com/css2?family=Great+Vibes&family=Gentium+Book+Plus:ital@1&family=Titillium+Web:ital,wght@1,400;1,600&family=Open+Sans:wght@400;700&family=Saira+Condensed:ital,wght@1,800&family=Saira:ital,wght@1,900&display=swap">
<style>
  :root {
    --frame: #000000;
    --paper: #f4f4f4;
    --sun: #f6d21c;
    --sun-light: #fbe98a;
    --sun-deep: #eeb900;
    --leaf: #8a9a3c;
    --wine: #7b1533;
    --wine-light: #8c1c3e;
    --ink: #1d1d1d;
    --white: #ffffff;
    --script-shade: rgba(120, 80, 0, 0.45);
  }
  * { box-sizing: border-box; margin: 0; padding: 0; }
  html, body { width: 1200px; height: 773px; overflow: hidden; background: var(--frame); }
  .card { position: relative; width: 1200px; height: 773px; background: var(--frame); overflow: hidden; }
  .card__inner { position: absolute; inset: 13px; overflow: hidden; }

  .sun-backdrop {
    position: absolute; inset: 0;
    background:
      radial-gradient(circle at 78% 30%, var(--sun-light) 0%, transparent 45%),
      radial-gradient(circle at 95% 80%, var(--sun-light) 0%, transparent 35%),
      linear-gradient(135deg, var(--sun) 0%, var(--sun-deep) 60%, var(--sun) 100%);
  }
  .divider-stripe {
    position: absolute; inset: 0; background: var(--leaf);
    clip-path: polygon(0 0, 473px 0, 715px 747px, 0 747px);
  }
  .paper-panel {
    position: absolute; inset: 0; background: var(--paper);
    clip-path: polygon(0 0, 467px 0, 706px 747px, 0 747px);
  }

  .brand { position: absolute; left: 44px; top: 58px; display: flex; align-items: center; gap: 14px; }
  .brand__dot { width: 44px; height: 44px; border-radius: 50%; background: var(--wine); }
  .brand__name { font-family: "Open Sans", sans-serif; font-weight: 700; font-size: 34px; color: var(--ink); letter-spacing: -0.5px; }

  .fruit-photo {
    position: absolute; left: 20px; top: 205px; width: 590px; height: 420px;
    border-radius: 45% 45% 40% 40%;
    background: radial-gradient(ellipse at 50% 50%, #f7c21a 0%, #f3ae12 45%, rgba(244, 244, 244, 0) 72%);
  }

  .effort-note {
    position: absolute; left: 37px; top: 683px; width: 640px;
    font-family: "Saira Condensed", sans-serif; font-style: italic; font-weight: 800;
    font-size: 27px; color: var(--wine); letter-spacing: 0.2px; white-space: nowrap;
  }

  .title {
    position: absolute; left: 530px; top: 36px; width: 640px;
    font-family: "Great Vibes", cursive; font-size: 104px; line-height: 1;
    color: var(--white); white-space: nowrap;
    text-shadow: 2px 3px 4px var(--script-shade);
  }
  .tagline {
    position: absolute; right: 37px; top: 172px;
    font-family: "Gentium Book Plus", serif; font-style: italic; font-size: 20px; color: #4a3a1a;
  }

  .fact {
    position: absolute; background: linear-gradient(90deg, var(--wine) 0%, var(--wine-light) 100%);
    border-radius: 0 26px 26px 0; color: var(--white); text-align: right;
    display: flex; flex-direction: column; justify-content: center;
  }
  .fact--nutrients { left: 575px; top: 315px; width: 450px; height: 89px; padding-right: 33px;
    font-family: "Titillium Web", sans-serif; font-style: italic; font-size: 24px; line-height: 1.55; }
  .fact--contrast { left: 615px; top: 425px; width: 465px; height: 57px; padding-right: 28px;
    font-family: "Titillium Web", sans-serif; font-style: italic; font-weight: 600; font-size: 26px; }
  .fact--sweet { left: 630px; top: 500px; width: 471px; height: 89px; padding-right: 36px;
    font-family: "Open Sans", sans-serif; }
  .fact--sweet .fact__lead { font-weight: 700; font-size: 35px; line-height: 1.2; }
  .fact--sweet .fact__sub { font-size: 24px; align-self: flex-start; padding-left: 155px; }
  .fact--juice { left: 660px; top: 605px; width: 473px; height: 104px; padding-right: 38px;
    font-family: "Saira", sans-serif; font-style: italic; font-weight: 900; font-size: 35px; line-height: 1.3;
    text-shadow: 2px 2px 2px rgba(0,0,0,0.5); }
</style>
</head>
<body>
<main class="card">
  <div class="card__inner">
    <div class="sun-backdrop" role="img" aria-label="Soft-focus photograph of bright yellow daisies"></div>
    <div class="divider-stripe"></div>
    <div class="paper-panel"></div>

    <header class="brand">
      <span class="brand__dot"></span>
      <span class="brand__name">Brightvale Cherries</span>
    </header>

    <div class="fruit-photo" role="img" aria-label="Photograph of three ripe golden Rainier cherries with green leaves"></div>

    <p class="effort-note">RAINIERS TAKE UP TO 4X AS MUCH WORK AS RED CHERRIES</p>

    <h1 class="title">Yellow Cherries</h1>
    <p class="tagline">yellow fruit (the blush on the skin is a kiss from the sun)</p>

    <div class="fact fact--nutrients">
      <span>Source of Vitamin C, Source of</span>
      <span>Potassium, and Source of Melatonin</span>
    </div>
    <div class="fact fact--contrast"><span>Add contrast to your summer table</span></div>
    <div class="fact fact--sweet">
      <span class="fact__lead">Sweetest Variety</span>
      <span class="fact__sub">- Still low glycemic</span>
    </div>
    <div class="fact fact--juice">
      <span>Juice doesn't stain</span>
      <span>Kid Friendly</span>
    </div>
  </div>
</main>
</body>
</html>
```